Business Card *

A business card design
Use the logo uploaded in the brief page.
You may use placeholders in your design layouts.
I will provide the actual business card details to the winning designer.

Logo
Place for contact info (name, title, phone, email, etc)

Requirements
Must have
• Logo

```html
<!DOCTYPE html>
<html lang="en">
<head>
<meta charset="utf-8">
<title>Kessane Business Card</title>
<link rel="stylesheet" href="https://fonts.googleapis.com/css2?family=Archivo:wdth,wght@125,600;125,700;125,800&display=swap">
<style>
  :root {
    --backdrop: #c8c8c8;
    --brand-green: #3bb54a;
    --card-white: #ffffff;
    --ink-grey: #939598;
  }
  * { margin: 0; padding: 0; box-sizing: border-box; }
  html, body { width: 1200px; height: 1000px; overflow: hidden; }
  body {
    background: var(--backdrop);
    font-family: "Archivo", Arial, sans-serif;
    font-stretch: 125%;
    position: relative;
  }
  .card { position: absolute; width: 685px; height: 381px; overflow: hidden; }

  .card-front { left: 39px; top: 50px; background: var(--brand-green); }
  .front-mark {
    position: absolute; left: 282px; top: 95px;
    width: 120px; height: 120px; border-radius: 50%;
    background: var(--card-white);
  }
  .front-name {
    position: absolute; left: 0; right: 0; top: 236px;
    text-align: center; color: var(--card-white);
    font-weight: 800; font-size: 43px; letter-spacing: 0.5px; line-height: 1;
  }

  .card-back { left: 474px; top: 463px; background: var(--card-white); }
  .contact { position: absolute; left: 101px; color: var(--ink-grey); font-weight: 700; }
  .contact-name { top: 96px; font-size: 41px; line-height: 1; font-weight: 800; }
  .contact-title { top: 136px; left: 102px; font-size: 14px; letter-spacing: 1.5px; }
  .contact-lines { top: 224px; font-size: 22px; line-height: 30px; }
  .social { position: absolute; left: 102px; top: 310px; display: flex; align-items: center; gap: 10px; }
  .social-square { width: 27px; height: 27px; background: var(--brand-green); }
  .social-name { color: var(--ink-grey); font-weight: 700; font-size: 19px; letter-spacing: 0.5px; }

  .back-mark {
    position: absolute; left: 398px; top: 72px;
    width: 282px; height: 282px; border-radius: 50%;
    border: 28px solid var(--ink-grey);
    display: flex; align-items: center; justify-content: center;
  }
  .back-mark-name { color: var(--brand-green); font-weight: 800; font-size: 30px; }
</style>
</head>
<body>
  <section class="card card-front">
    <div class="front-mark"></div>
    <div class="front-name">KESSANE</div>
  </section>

  <section class="card card-back">
    <div class="contact contact-name">NAME</div>
    <div class="contact contact-title">TITLE</div>
    <div class="contact contact-lines">PHONE<br>EMAIL</div>
    <div class="social">
      <span class="social-square"></span>
      <span class="social-name">KESSANE</span>
    </div>
    <div class="back-mark"><span class="back-mark-name">KESSANE</span></div>
  </section>
</body>
</html>
```